Brightwire Hollow Business cards

one side I would like my logo (uploaded) and the other side I want my details. I'm an electrician in sydney. The logo side I'm happy with just a white background and our logo in the middle.

Details for other side
24/7 Sydney Electrician
Marcus Pell
0431 587 219
marcus@brightwirehollow.com.au
brightwirehollow.com.au
icons for facebook, instagram, linked in

Industry/Entity Type

electrician

Contact Information for Business Card

company info

```html
<!DOCTYPE html>
<html lang="en">
<head>
<meta charset="utf-8">
<title>Brightwire Hollow – Business Cards</title>
<link rel="stylesheet" href="https://fonts.googleapis.com/css2?family=Quicksand:wght@300;400;500;700&display=swap">
<style>
  :root {
    --backdrop: #2f2628;
    --card-white: #f1f1f0;
    --brand-red: #b02e12;
    --brand-red-deep: #982610;
    --logo-red: #c9352b;
    --ink: #121212;
    --slate: #3a3a3a;
    --paper: #ffffff;
  }
  * { margin: 0; padding: 0; box-sizing: border-box; }
  html, body {
    width: 1200px; height: 1094px; overflow: hidden;
    background: var(--backdrop);
    font-family: "Quicksand", sans-serif;
  }
  .sheet {
    width: 1200px; height: 1094px;
    display: flex; flex-direction: column; align-items: center; justify-content: center;
    gap: 40px;
  }
  .card {
    position: relative;
    width: 840px; height: 480px;
    border-radius: 22px;
    overflow: hidden;
  }

  /* Logo side */
  .card--front { background: var(--card-white); }
  .brand-name {
    position: absolute; left: 0; right: 0; top: 170px;
    text-align: center;
    font-size: 66px; font-weight: 700; letter-spacing: 1px;
    color: var(--logo-red);
    text-transform: uppercase;
  }
  .front-web {
    position: absolute; right: 60px; bottom: 50px;
    font-size: 34px; font-weight: 300; letter-spacing: 0.5px;
    color: var(--slate);
  }
  .front-web .accent { color: var(--logo-red); }

  /* Details side */
  .card--back { background: var(--brand-red); }
  .art-area {
    position: absolute;
    background: linear-gradient(135deg, var(--brand-red-deep), var(--brand-red));
  }
  .art-area--cord-side { left: 0; top: 0; width: 120px; height: 380px; }
  .art-area--cord-base { left: 0; bottom: 0; width: 500px; height: 100px; }
  .rule { position: absolute; width: 4px; }
  .rule--top { background: var(--ink); right: 46px; top: 0; height: 160px; }
  .rule--bottom { background: var(--paper); right: 46px; bottom: 0; height: 180px; }
  .identity {
    position: absolute; right: 72px; top: 26px; text-align: right;
  }
  .person-name {
    font-size: 46px; font-weight: 700; letter-spacing: 1px;
    color: var(--paper); text-transform: uppercase; line-height: 1.1;
  }
  .role {
    margin-top: 6px;
    font-size: 25px; font-weight: 500; letter-spacing: 0.5px;
    color: var(--ink); text-transform: uppercase;
  }
  .contact {
    position: absolute; right: 72px; top: 290px; text-align: right;
  }
  .phone {
    font-size: 58px; font-weight: 400; letter-spacing: 1px;
    color: var(--paper); line-height: 1.05;
  }
  .email {
    margin-top: 2px;
    font-size: 27px; font-weight: 500; color: var(--ink);
  }
  .socials {
    margin-top: 12px;
    display: flex; justify-content: flex-end; gap: 10px;
  }
  .social-dot {
    width: 38px; height: 38px; border-radius: 50%;
    background: var(--ink);
  }
</style>
</head>
<body>
  <main class="sheet">
    <section class="card card--front" aria-label="Business card, logo side">
      <div class="brand-name">Brightwire Hollow</div>
      <div class="front-web"><span class="accent">brightwire</span>hollow.com.au</div>
    </section>

    <section class="card card--back" aria-label="Business card, details side">
      <div class="art-area art-area--cord-side" role="img" aria-label="Illustration of a black plug with its cord running down the card edge"></div>
      <div class="art-area art-area--cord-base" role="img" aria-label="Illustration of a white plug with its cord running along the card base"></div>

      <span class="rule rule--top"></span>
      <span class="rule rule--bottom"></span>

      <div class="identity">
        <div class="person-name">Marcus Pell</div>
        <div class="role">24/7 Sydney Electrician</div>
      </div>

      <div class="contact">
        <div class="phone">0431 587 219</div>
        <div class="email">marcus@brightwirehollow.com.au</div>
        <div class="socials" aria-label="Social media profiles">
          <span class="social-dot"></span>
          <span class="social-dot"></span>
          <span class="social-dot"></span>
        </div>
      </div>
    </section>
  </main>
</body>
</html>
```